Website Home Page Graphics / Banner

We need a Website Home page banner or graphic that is engaging and describes what we do with either words or a graphic story- which is Screen Print & Create promotional products. I love the minimalist design style, but I also want the home page to be descriptive and inviting which I feel it is not. Here is a link to our current website www.brambleinkworks.com Our current tagline is
"Here at Bramble Inkworks, we take a personal approach to screen-printing. Let us support you in creating a product that leaves a lasting impression."
We are sticking with the Black, White, Grey & Green theme as seen on the website. Attached are some photos that inspire me / I would like to replicate in some way on my own home page.

Target Market(s)

Anybody who needs Promotional Products. Although we can relate most to small Businesses and the younger (age 19-35) demographic

Font styles to use
Other font styles liked:
• Heritage, Helvetica Neu - those are my current fonts

Colors
86cfc6
ffffff
c6c6c6
000000
919191

Requirements
Must have
• Engaging Graphic Story that describes in either pictures or words what we do.
Nice to have
• Warm inviting design

```html
<!DOCTYPE html>
<html lang="en">
<head>
<meta charset="UTF-8">
<title>How It Works – Bramble Inkworks</title>
<link href="https://fonts.googleapis.com/css2?family=Roboto:wght@500;700&display=swap" rel="stylesheet">
<style>
  :root {
    --page-bg: #ffffff;
    --foliage-light: #8fb33a;
    --foliage-dark: #3f6a1f;
    --water-top: #7a7f74;
    --water-mid: #9aa4a3;
    --water-deep: #4f5c5c;
    --band-tint: rgba(40, 45, 45, 0.28);
    --title-green: #14c796;
    --title-outline: #ffffff;
    --title-shadow: #2b2b2b;
    --disc-light: #ffffff;
    --disc-mid: #c6c6c6;
    --disc-dark: #919191;
    --disc-rim: #ffffff;
    --disc-text: #333333;
    --splash-light: #6fd3f2;
    --splash-dark: #1a7fc0;
  }
  * { margin: 0; padding: 0; box-sizing: border-box; }
  html, body { width: 1200px; height: 1200px; overflow: hidden; background: var(--page-bg); }
  .canvas { position: relative; width: 1200px; height: 1200px; background: var(--page-bg); font-family: "Roboto", Arial, sans-serif; }

  .banner { position: absolute; left: 0; top: 238px; width: 1200px; height: 678px; overflow: hidden; }
  .banner-scene {
    position: absolute; inset: 0;
    background: linear-gradient(180deg,
      var(--foliage-light) 0%, var(--foliage-dark) 38%,
      var(--water-top) 55%, var(--water-mid) 75%, var(--water-deep) 100%);
  }
  .steps-band { position: absolute; left: 0; top: 234px; width: 1200px; height: 304px; background: var(--band-tint); }

  .banner-title {
    position: absolute; left: 0; right: 0; top: 44px; text-align: center;
    font-weight: 700; font-size: 100px; letter-spacing: -3px; line-height: 1;
    color: var(--title-green);
    text-shadow:
      2px 0 0 var(--title-outline), -2px 0 0 var(--title-outline),
      0 2px 0 var(--title-outline), 0 -2px 0 var(--title-outline),
      2px 2px 0 var(--title-outline), -2px -2px 0 var(--title-outline),
      2px -2px 0 var(--title-outline), -2px 2px 0 var(--title-outline),
      5px 5px 0 var(--title-shadow);
  }

  .step { position: absolute; top: 278px; width: 236px; height: 236px; }
  .step-disc {
    position: absolute; inset: 0; z-index: 1; border-radius: 50%;
    border: 5px solid var(--disc-rim);
    background: radial-gradient(circle at 50% 45%, var(--disc-light) 0%, var(--disc-mid) 45%, var(--disc-dark) 100%);
    box-shadow: 3px 4px 8px rgba(0,0,0,0.35);
    display: flex; align-items: center; justify-content: center; text-align: center;
    color: var(--disc-text); font-weight: 500; font-size: 32px; line-height: 39px;
    padding-top: 12px;
  }
  .step-disc.is-print { padding-top: 0; }
  .step-disc.is-list { align-items: flex-start; padding-top: 31px; line-height: 38px; }
  .step-splash {
    position: absolute; z-index: 2; left: 24px; bottom: -20px; width: 188px; height: 66px;
    border-radius: 40% 40% 50% 50% / 30% 30% 70% 70%;
    background: linear-gradient(180deg, var(--splash-light), var(--splash-dark));
  }
  .step-brand { left: 108px; }
  .step-print { left: 484px; }
  .step-products { left: 860px; }
</style>
</head>
<body>
<main class="canvas">
  <section class="banner">
    <div class="banner-scene" role="img" aria-label="Photo of a jungle river with a waterfall surrounded by green forest"></div>
    <div class="steps-band"></div>
    <h1 class="banner-title">HOW IT WORKS</h1>

    <div class="step step-brand">
      <div class="step-disc">YOUR BRAND<br>OR LOGO</div>
      <div class="step-splash" role="img" aria-label="Blue water splash"></div>
    </div>
    <div class="step step-print">
      <div class="step-disc is-print">PRINTED TO</div>
      <div class="step-splash" role="img" aria-label="Blue water splash"></div>
    </div>
    <div class="step step-products">
      <div class="step-disc is-list">SHIRTS<br>MUGS<br>BAGS<br>ETC.</div>
      <div class="step-splash" role="img" aria-label="Blue water splash"></div>
    </div>
  </section>
</main>
</body>
</html>
```